Consulting Firm stationery design

Now that the MakerHive has given us a new logo we'll now need to have all our stationery designed. So we're asking for this community to help us once again.We're looking to get from you Letterheads (Header and Footer, suitable to be applied on a .docx format. Vectors are required but keep this in mind), Envelopes (Front and Back designs, back is not a must but desirable depending on your design), 9"x 12" Pocket Folders (consider design for front and back, also for pockets as well), Business Cards.An elegant design is a must have, mostly for Folders and Envelopes. The idea with this two is to stand out from others when they're handed over. Ideas are welcomed, we were thinking maybe on some texturing simulation for these.Folders will have 3 addresses and contact information. Envelopes will have 1 address and contact information.Brand Manual attached. vendaluxo logo has been copyrighted already. I'm also attaching the current stationary designs (these never got to be out for production but was going to be before we made the brand changes); Pocker folders page 1 to 4 (pages 2 and 4 are the pocket designs), Pages 5 and 6 (6 is the back of the envelope), Pages 7 and 8 (8 is the back of the business card). No letterhead within these designs as it just had the logo and address.

Industry/Entity Type

Business Consultant

Font styles to use
Serif
Sans Serif

Requirements
Must have
• Elegance
Nice to have
• Modern looking out of common

```html
<!DOCTYPE html>
<html lang="es">
<head>
<meta charset="utf-8">
<title>Folder Design — vendaluxo</title>
<link rel="stylesheet" href="https://fonts.googleapis.com/css2?family=Montserrat:wght@300;400;600;700&display=swap">
<style>
  :root {
    --ink: #111111;
    --paper: #ffffff;
    --slate: #353640;
    --brand-blue: #127fba;
    --pattern-blue: #3d72a6;
    --pattern-mix: #384e6c;
    --light: #e6e6e6;
    --rule: #8a8a8a;
  }
  * { margin: 0; padding: 0; box-sizing: border-box; }
  html, body { width: 958px; height: 1200px; overflow: hidden; background: var(--paper); }
  body { position: relative; font-family: "Montserrat", sans-serif; color: var(--ink); }

  .sheet-title {
    position: absolute; left: 33px; top: 30px;
    font-size: 15.5px; font-weight: 700; letter-spacing: 0.3px;
  }

  .cover {
    position: absolute; top: 109px; width: 348px; height: 464px;
    background: var(--slate); overflow: hidden;
  }
  .cover--front { left: 106px; }
  .cover--back { left: 503px; }

  /* Brand pattern zone: soft gradient in the pattern's blue and slate tones */
  .brand-pattern {
    position: absolute;
    background: radial-gradient(ellipse at 35% 40%, var(--pattern-mix) 0%, var(--pattern-blue) 70%, var(--pattern-mix) 100%);
    opacity: 0.9;
  }
  .cover--front .brand-pattern { left: 0; top: 157px; width: 291px; height: 307px; }
  .cover--back .brand-pattern { left: 0; top: 0; width: 291px; height: 307px; }

  .wordmark {
    position: absolute; font-weight: 700; color: var(--brand-blue);
    letter-spacing: -0.3px; line-height: 1;
  }
  .cover--front .wordmark { left: 247px; top: 38px; font-size: 17px; }
  .cover--back .wordmark { left: 23px; top: 355px; font-size: 15px; }

  .contact {
    position: absolute; left: 24px; top: 390px;
    font-size: 5px; font-weight: 300; line-height: 1.15; color: var(--light);
  }

  .offices {
    position: absolute; left: 23px; top: 420px; width: 310px; height: 27px;
  }
  .office {
    position: absolute; top: 0; height: 27px;
    border-left: 1.2px solid var(--light);
    padding-left: 4px; padding-top: 2px;
    font-size: 4.6px; font-weight: 300; line-height: 1.25; color: var(--light);
    white-space: nowrap;
  }
  .office strong { font-weight: 600; display: block; }
  .office--admin { left: 0; }
  .office--sales { left: 113px; }
  .office--ops { left: 218px; }

  .pocket-spread {
    position: absolute; left: 130px; top: 653px; width: 697px; height: 464px;
  }
  .pocket {
    position: absolute; top: 0; width: 348px; height: 464px;
    border: 0.8px solid var(--rule); border-bottom: none; background: var(--paper);
  }
  .pocket--left { left: 0; }
  .pocket--right { left: 349px; }
  .pocket__band {
    position: absolute; left: 0; right: 0; bottom: 0; height: 155px;
    background: var(--brand-blue);
  }
  .spine {
    position: absolute; left: 348px; top: 0; width: 1.2px; height: 464px; background: var(--rule);
  }

  .pocket__mark {
    position: absolute; left: 140px; top: 22px;
    font-size: 14px; font-weight: 700; color: var(--paper); line-height: 1;
  }

  .partners {
    position: absolute; left: 47px; bottom: 20px;
    display: flex; align-items: center; gap: 22px;
    color: var(--paper); font-weight: 700; font-size: 15px; line-height: 1;
  }
  .partner { display: flex; align-items: center; gap: 5px; }
  .partner__square { width: 18px; height: 18px; background: var(--paper); }
  .partner--small { font-size: 11px; }
</style>
</head>
<body>
  <h1 class="sheet-title">FOLDER DESIGN</h1>

  <section class="cover cover--front">
    <div class="brand-pattern" role="img" aria-label="Large diagonal-striped brand pattern in blue on slate"></div>
    <div class="wordmark">vendaluxo</div>
  </section>

  <section class="cover cover--back">
    <div class="brand-pattern" role="img" aria-label="Large diagonal-striped brand pattern in blue on slate"></div>
    <div class="wordmark">vendaluxo</div>
    <div class="contact">
      (555) 204-7710<br>
      info@vendaluxo.do<br>
      www.vendaluxo.do
    </div>
    <div class="offices">
      <div class="office office--admin">
        <strong>Oficina Administrativa</strong>
        Alameda Business Center<br>
        Calle Los Robles 42, Serralles<br>
        Santo Domingo, Rep. Dominicana
      </div>
      <div class="office office--sales">
        <strong>Ventas Globales</strong>
        1180 Harbor View Drive, Suite 4C<br>
        Dover, Delaware 19901<br>
        United States
      </div>
      <div class="office office--ops">
        <strong>Operaciones</strong>
        Torre Meridian Plaza<br>
        Av. Las Américas 27, Naco<br>
        Santo Domingo, Rep. Dominicana
      </div>
    </div>
  </section>

  <section class="pocket-spread">
    <div class="pocket pocket--left">
      <div class="pocket__band">
        <div class="pocket__mark">vendaluxo</div>
      </div>
    </div>
    <div class="pocket pocket--right">
      <div class="pocket__band">
        <div class="partners">
          <span class="partner">Ledgerly</span>
          <span class="partner"><span class="partner__square"></span>Cloudmere</span>
          <span class="partner partner--small">Finvera</span>
        </div>
      </div>
    </div>
    <div class="spine"></div>
  </section>
</body>
</html>
```